quiet meadow therapy (QMT)

I need to build a website for my therapy business.
There are two parts to the website
on the landing page; they choose whether they are therapists making a referral or patients needing more information.
After that, they are taken to their respective pages.
There is the textual information and a referral form on the therapist page, and on the patient page, the text is a bit different, and there will be a booking page on the patient page.
Visually minimal, it's a therapeutic website. I want it clean, clinical, and modern
colors: greenish blue or maybe orangish
PHP/html code
Updates

Hi everyone
I'm very sorry for the lack of responses to your designs. I am trying to work it out, but this platform has been a challenge for me.
I appreciate everyone's efforts, and I am unsure how to rate designs and move forward with the ones I like. There is a 5-star rating, but I don't understand how I'm supposed to politely say that it is not it without feeling like I'm going to affect someone's future rating negatively.
Please understand me. Thank you

Designs look the same

Target Market(s)

therapy and stress management

Industry/Entity Type

stress management therapy

Coding

Coded - Design and coding required

Number of Pages Required

5+ page

Font styles to use
Serif

Colors
0094D4
00A9DD
6FCCEA
C7EBF8
E9F6FB
00AB8E
00BBA5
67D7C9
C6EFE9
E9F9F6

Requirements
Must have
• landing page that that have 2 options. one for therapist another for patient

```html
<!DOCTYPE html>
<html lang="en">
<head>
<meta charset="utf-8">
<title>Quiet Meadow Therapy</title>
<link href="https://fonts.googleapis.com/css2?family=Merriweather:wght@400;700&family=Montserrat:wght@400;500;600;700&display=swap" rel="stylesheet">
<style>
:root{
  --teal:#17a898;
  --teal-soft:#e9f9f6;
  --orange:#f39200;
  --ink:#2e2e2e;
  --text:#3d3d3d;
  --muted:#7a7a7a;
  --line:#d6d6d6;
  --wash:#f6f8fc;
  --white:#ffffff;
}
*{margin:0;padding:0;box-sizing:border-box}
html,body{width:1200px;height:3978px;overflow:hidden}
body{position:relative;background:var(--white);font-family:"Montserrat",sans-serif;color:var(--text)}
.abs{position:absolute}
.serif{font-family:"Merriweather",serif}
.eyebrow{font-size:17px;font-weight:500;color:var(--orange);letter-spacing:.3px}
.h2{font-family:"Merriweather",serif;font-size:42px;color:var(--ink);font-weight:400;white-space:nowrap}
.h2 b{font-weight:700}
.h2 .accent{color:var(--teal)}
.body-copy{font-size:14px;line-height:21px;color:var(--text)}
.btn{position:absolute;height:44px;border-radius:22px;color:#fff;font-size:13px;font-weight:700;display:flex;align-items:center;justify-content:center;letter-spacing:.3px;text-decoration:none}
.btn-orange{background:var(--orange)}
.btn-teal{background:var(--teal)}
.photo{position:absolute}

/* header */
.logo{position:absolute;display:flex;align-items:center;gap:12px}
.logo-dot{width:30px;height:30px;border-radius:50%;background:var(--teal)}
.logo-name{font-family:"Montserrat",sans-serif;font-size:34px;font-weight:600;letter-spacing:10px}
.nav a{position:absolute;top:33px;font-size:13px;color:var(--text);text-decoration:none}
.nav a.current{font-weight:600;color:var(--ink)}
.login-link{position:absolute;top:24px;padding-left:10px;height:34px}
.login-link .l1{font-family:"Merriweather",serif;font-size:12px;text-decoration:underline}
.login-link .l2{font-size:10px;color:var(--muted);margin-top:3px}

/* feature card */
.feature-card{left:105px;top:584px;width:988px;height:154px;background:#fff;border-radius:16px;box-shadow:0 4px 18px rgba(0,0,0,.12)}
.feature{position:absolute;top:24px}
.feature h4{font-size:13px;font-weight:700;color:var(--ink);margin-top:12px}
.feature p{font-size:12px;color:var(--muted);line-height:19px;margin-top:4px;width:190px}

/* service cards */
.service-card{position:absolute;top:851px;width:175px;height:230px;border:1.5px dashed #bdbdbd;border-radius:14px;text-align:center}
.service-card .inner{position:absolute;inset:6px;border-radius:10px;padding-top:22px}
.service-card h5{font-family:"Merriweather",serif;font-size:13px;font-weight:700;color:var(--ink);margin-top:12px}
.service-card p{font-size:11.5px;line-height:17.5px;color:var(--muted);margin:6px auto 0;width:140px}
.service-card.active .inner{background:var(--teal)}
.service-card.active h5,.service-card.active p{color:#fff}

/* about copy */
.about-copy{font-size:13px;line-height:21px;color:var(--text);width:375px}

/* blog */
.post{position:absolute;top:3053px;width:190px;height:251px;background:#fff;border-radius:6px;box-shadow:0 3px 14px rgba(0,0,0,.1);overflow:hidden}
.post .thumb{height:147px}
.post .date{position:absolute;left:14px;top:136px;background:var(--orange);color:#fff;font-size:10px;padding:3px 8px;border-radius:10px}
.post h6{font-size:13px;font-weight:700;color:var(--ink);margin:21px 0 0 15px}
.post p{font-size:11px;line-height:15px;color:var(--muted);margin:6px 14px 0 15px}
.post a{display:block;font-size:11px;color:var(--orange);text-decoration:underline;margin:6px 0 0 15px}

/* footer */
.footer{left:0;top:3755px;width:1200px;height:223px;background:var(--teal);color:#fff}
.footer a{color:#fff;text-decoration:none}
.footer .col a{position:absolute;font-size:13px}
.footer .log a{position:absolute;font-family:"Merriweather",serif;font-size:12px;text-decoration:underline}
.social{position:absolute;top:3942px;width:24px;height:24px;border:1.5px solid #fff;border-radius:50%}
</style>
</head>
<body>

<!-- header -->
<header>
  <div class="logo" style="left:99px;top:16px">
    <span class="logo-dot"></span>
    <span class="logo-name" style="color:var(--ink)">QMT</span>
  </div>
  <nav class="nav">
    <a class="current" style="left:411px">Home</a>
    <a style="left:491px">Services</a>
    <a style="left:584px">Articles</a>
  </nav>
  <div class="login-link" style="left:726px;border-left:2px solid var(--orange)">
    <div class="l1" style="color:var(--orange)">Login &nbsp;As A Therapists</div>
    <div class="l2">Lorem ipsum dolor sit amet consectetur</div>
  </div>
  <div class="login-link" style="left:960px;border-left:2px solid var(--teal)">
    <div class="l1" style="color:var(--teal)">Login &nbsp;As A Patient</div>
    <div class="l2">Lorem ipsum dolor sit amet</div>
  </div>
</header>

<!-- hero -->
<section class="hero">
  <div class="photo" role="img" aria-label="Photo of a thoughtful woman in a counselling session" style="left:0;top:78px;width:1200px;height:572px;background:linear-gradient(90deg,#f2f2f2 0%,#f0efee 42%,#d9cbbd 62%,#8aa0b8 80%,#e3e4e8 100%)"></div>
  <div class="abs eyebrow" style="left:99px;top:236px;font-size:22px">Welcome To</div>
  <div class="abs" style="left:265px;top:248px;width:148px;height:1.5px;background:var(--teal)"></div>
  <h1 class="abs serif" style="left:99px;top:265px;font-size:52px;line-height:62px;font-weight:400;color:var(--ink);white-space:nowrap">Quiet Meadow<br><b style="font-weight:700">Therapy</b></h1>
  <p class="abs" style="left:99px;top:400px;width:400px;font-size:11.5px;line-height:18px;color:var(--text)">Lorem ipsum dolor sit amet, consectetur adipiscing elit. Placerat diam nunc nullam faucibus vitae eget venenatis nunc.</p>
  <a class="btn btn-orange" style="left:99px;top:463px;width:127px">THERAPIST</a>
  <a class="btn btn-teal" style="left:241px;top:463px;width:109px">PATIENT</a>
</section>

<div class="abs feature-card">
  <div class="feature" style="left:71px">
    <svg width="36" height="36" viewBox="0 0 36 36" fill="none" stroke="#333" stroke-width="1.5"><path d="M3 10h18c3 0 3 4 0 4h-8M3 26h10l14-6c3-1 4 3 1 4l-14 7H3"/><circle cx="20" cy="19" r="4" stroke="var(--orange)"/></svg>
    <h4>Affordable for Anyone</h4>
    <p>Lorem ipsum dolor sit amet consectetur</p>
  </div>
  <div class="feature" style="left:398px">
    <svg width="36" height="36" viewBox="0 0 36 36" fill="none" stroke="#333" stroke-width="1.5"><path d="M18 4l12 5v9c0 8-6 12-12 14C12 30 6 26 6 18V9z"/><path d="M13 18l4 4 7-8" stroke="var(--orange)"/></svg>
    <h4>Qualified Services</h4>
    <p>Lorem ipsum dolor sit amet consectetur</p>
  </div>
  <div class="feature" style="left:727px">
    <svg width="52" height="36" viewBox="0 0 52 36" fill="none" stroke="#333" stroke-width="1.5"><circle cx="14" cy="10" r="6"/><circle cx="38" cy="10" r="6"/><circle cx="26" cy="16" r="6" stroke="var(--orange)"/><path d="M3 32c0-8 5-12 11-12M49 32c0-8-5-12-11-12M15 34c0-7 5-11 11-11s11 4 11 11"/></svg>
    <h4>Supportive Staff</h4>
    <p>Lorem ipsum dolor sit amet consectetur</p>
  </div>
  <div class="abs" style="left:357px;top:151px;width:276px;height:3px;background:var(--teal)"></div>
</div>

<!-- services -->
<section class="services">
  <div class="abs eyebrow" style="left:107px;top:829px">SERVICES</div>
  <h2 class="abs h2" style="left:107px;top:852px"><b>Services</b> <span class="accent">We Offer</span></h2>
  <p class="abs" style="left:107px;top:922px;width:385px;font-size:13px;line-height:21px">Lorem ipsum dolor sit amet, consectetur adipiscing elit. Sit fermentum dui mauris egestas tristique pellentesque quis. Nibh ut natoque vestibulum fringilla consequat arcu non tortor.</p>
  <a class="btn btn-orange" style="left:106px;top:1031px;width:169px">BOOK A SERVICE</a>

  <div class="service-card" style="left:517px"><div class="inner">
    <svg width="34" height="48" viewBox="0 0 34 48" fill="var(--teal)"><circle cx="17" cy="8" r="7"/><path d="M6 20q11-6 22 0v14h-5v14h-12V34H6z"/></svg>
    <h5>Individual Therapy</h5>
    <p>Lorem ipsum dolor sit amet, consectetur adipiscing elit. Sit fermentum dui mauris egestas</p>
  </div></div>
  <div class="service-card active" style="left:718px"><div class="inner">
    <svg width="44" height="48" viewBox="0 0 44 48" fill="#fff"><circle cx="13" cy="7" r="5"/><circle cx="31" cy="7" r="5"/><path d="M4 18q9-6 16 0v28h-6V32H8zM24 18q9-6 16 0l-4 14v14h-6z"/><path d="M22 30c-3-3-6 0-3 3l3 3 3-3c3-3 0-6-3-3z" fill="var(--teal)"/></svg>
    <h5>Couple Therapy</h5>
    <p>Lorem ipsum dolor sit amet, consectetur adipiscing elit. Sit fermentum dui mauris egestas</p>
  </div></div>
  <div class="service-card" style="left:919px"><div class="inner">
    <svg width="44" height="48" viewBox="0 0 44 48" fill="var(--teal)"><circle cx="22" cy="6" r="5"/><circle cx="10" cy="20" r="5"/><circle cx="34" cy="20" r="5"/><circle cx="22" cy="28" r="5"/><path d="M15 18h14v6H15zM2 34q8-6 16 0v12H2zM26 34q8-6 16 0v12H26zM14 38h16v8H14z"/></svg>
    <h5>Group Therapy</h5>
    <p>Lorem ipsum dolor sit amet, consectetur adipiscing elit. Sit fermentum dui mauris egestas</p>
  </div></div>
</section>

<!-- about -->
<section class="about">
  <div class="abs" style="left:103px;top:1223px;width:294px;height:366px;background:var(--teal);border-top-right-radius:28px"></div>
  <div class="photo" role="img" aria-label="Photo of a therapist taking notes during a session with a client" style="left:136px;top:1260px;width:364px;height:231px;border-radius:10px;background:linear-gradient(120deg,#d8d4cf,#b9b3ab 45%,#e7e3dd)"></div>
  <div class="abs serif" style="left:176px;top:1517px;font-size:13.5px;line-height:21px;color:#fff">FOR PRACTICE<br>PROFESSIONALS</div>
  <div class="abs" style="left:369px;top:1434px;width:189px;height:192px;background:#fff;box-shadow:0 3px 12px rgba(0,0,0,.18)"></div>
  <div class="photo" role="img" aria-label="Portrait photo of a smiling woman outdoors" style="left:375px;top:1440px;width:177px;height:180px;background:linear-gradient(160deg,#6f8a4e,#a7b98a 50%,#9fb3d1)"></div>

  <div class="abs eyebrow" style="left:636px;top:1232px">ABOUT</div>
  <h2 class="abs h2" style="left:636px;top:1258px"><b>Who</b> <span class="accent">We Are</span></h2>
  <p class="abs about-copy" style="left:636px;top:1324px">Lorem ipsum dolor sit amet, consectetur adipiscing elit. Sit fermentum dui mauris egestas tristique pellentesque quis. Nibh ut natoque vestibulum fringilla consequat arcu non tortor. Nullam pulvinar feugiat id tortor risus pharetra nisl eros, felis. Habitant eget ut nunc lobortis nec, ultrices vitae mattis.</p>
  <p class="abs about-copy" style="left:636px;top:1470px">Lorem ipsum dolor sit amet, consectetur adipiscing elit. Sit fermentum dui mauris egestas tristique pellentesque quis. Nibh ut natoque vestibulum fringilla consequat arcu non tortor.</p>
</section>

<!-- specialists -->
<section class="specialists">
  <div class="abs" style="left:0;top:1691px;width:1200px;height:633px;background:var(--wash)"></div>
  <div class="abs" style="left:882px;top:2074px;width:200px;height:200px;border-radius:50%;border:26px solid #e8eefa"></div>
  <div class="abs eyebrow" style="left:0;width:1200px;top:1740px;text-align:center">STRESS THERAPY</div>
  <h2 class="abs h2" style="left:0;width:1200px;top:1767px;text-align:center">Our &nbsp;Stress Therapy <b class="accent">Specialists</b></h2>
  <div class="photo" role="img" aria-label="Video still of a therapist talking with a family on a sofa" style="left:215px;top:1848px;width:769px;height:383px;border-radius:4px;box-shadow:0 4px 16px rgba(0,0,0,.15);background:linear-gradient(110deg,#cdb89c,#e6dccf 35%,#d3643f 55%,#7c8ca3 75%,#bfae98)"></div>
  <div class="abs serif" style="left:258px;top:2115px;transform:rotate(-90deg);transform-origin:left top;font-size:20px;font-weight:700;color:#fff;white-space:nowrap">Play Video</div>
  <svg class="abs" style="left:242px;top:2142px" width="64" height="64" viewBox="0 0 64 64"><circle cx="32" cy="32" r="32" fill="var(--orange)"/><path d="M26 21l18 11-18 11z" fill="#fff"/></svg>
</section>

<!-- staff -->
<section class="staff">
  <div class="abs eyebrow" style="left:0;width:1200px;top:2390px;text-align:center">BECOME A MEMBER</div>
  <h2 class="abs h2" style="left:0;width:1200px;top:2412px;text-align:center">Our &nbsp;Friendly <b class="accent">Staff</b></h2>
  <p class="abs" style="left:103px;top:2491px;width:460px;font-size:13px;line-height:21px">Lorem ipsum dolor sit amet, consectetur adipiscing elit. Sit fermentum dui mauris egestas tristique pellentesque quis. Nibh ut natoque vestibulum fringilla consequat arcu non tortor. Nullam pulvinar feugiat id tortor risus pharetra nisl eros, felis. Habitant eget ut nunc lobortis nec, ultrices vitae mattis.</p>
  <p class="abs" style="left:630px;top:2491px;width:420px;font-size:13px;line-height:21px">Lorem ipsum dolor sit amet, consectetur adipiscing elit. Sit fermentum dui mauris egestas tristique pellentesque quis.</p>
  <a class="btn btn-orange" style="left:630px;top:2564px;width:213px">LOGIN AS A THERAPIST</a>
  <div class="photo" role="img" aria-label="Group photo of six smiling staff members" style="left:136px;top:2617px;width:883px;height:298px;background:linear-gradient(90deg,#3f5fa8,#c9b6a4 25%,#6b4a6a 40%,#e6e6e6 55%,#37506e 70%,#8a8a66 90%,#b79a84);border-radius:120px 120px 0 0"></div>
</section>

<!-- blog -->
<section class="blog">
  <div class="abs" style="left:0;top:2918px;width:1200px;height:502px;background:linear-gradient(180deg,#ffffff,#f7f8f8 50%,#ffffff)"></div>
  <div class="abs eyebrow" style="left:103px;top:3088px">ARTICLES</div>
  <h2 class="abs h2" style="left:103px;top:3112px"><b>Recent</b> <span class="accent">Blog</span></h2>
  <p class="abs" style="left:103px;top:3174px;width:345px;font-size:13px;line-height:21px">Lorem ipsum dolor sit amet, consectetur adipiscing elit. Sit fermentum dui mauris egestas tristique pellentesque quis.</p>
  <svg class="abs" style="left:103px;top:3256px" width="80" height="34" viewBox="0 0 80 34"><circle cx="17" cy="17" r="17" fill="#ddd"/><path d="M23 17H11m4-4l-4 4 4 4" stroke="#fff" stroke-width="1.5" fill="none"/><circle cx="62" cy="17" r="17" fill="var(--orange)"/><path d="M56 17h12m-4-4l4 4-4 4" stroke="#fff" stroke-width="1.5" fill="none"/></svg>

  <article class="post" style="left:480px">
    <div class="thumb" role="img" aria-label="Photo of a smiling blonde woman" style="background:linear-gradient(160deg,#7f9a5b,#b8c7d8)"></div>
    <span class="date">01 &nbsp;AUG 2022</span>
    <h6>Lorem ipsum dolor</h6>
    <p>Lorem ipsum dolor sit amet, consectetur adipiscing elit.</p>
    <a>READ MORE</a>
  </article>
  <article class="post" style="left:692px">
    <div class="thumb" role="img" aria-label="Photo of a group joining hands in a circle" style="background:linear-gradient(160deg,#9a9a9a,#e0e0e0 50%,#7d6a5d)"></div>
    <span class="date">01 &nbsp;AUG 2022</span>
    <h6>Lorem ipsum dolor</h6>
    <p>Lorem ipsum dolor sit amet, consectetur adipiscing elit.</p>
    <a>READ MORE</a>
  </article>
  <article class="post" style="left:903px">
    <div class="thumb" role="img" aria-label="Photo of a smiling woman with long hair" style="background:linear-gradient(160deg,#caa78f,#f0e6dc 55%,#9a6a55)"></div>
    <span class="date">01 &nbsp;AUG 2022</span>
    <h6>Lorem ipsum dolor</h6>
    <p>Lorem ipsum dolor sit amet, consectetur adipiscing elit.</p>
    <a>READ MORE</a>
  </article>
</section>

<!-- login cta -->
<section class="login-cta">
  <div class="abs" style="left:1093px;top:3576px;width:107px;height:179px;background:var(--teal)"></div>
  <div class="abs" style="left:0;top:3423px;width:1093px;height:332px;background:#fff;border-top-right-radius:16px;box-shadow:0 -4px 16px rgba(0,0,0,.06)"></div>
  <div class="abs eyebrow" style="left:0;width:1200px;top:3487px;text-align:center">LOGIN AS</div>
  <p class="abs serif" style="left:230px;width:740px;top:3515px;text-align:center;font-size:28px;line-height:37px;color:var(--ink)">Lorem ipsum dolor sit amet, consectetur adipiscing elit. Sit fermentum dui mauris egestas tristique pellentesque quis.</p>
  <a class="btn btn-orange" style="left:474px;top:3654px;width:127px">THERAPIST</a>
  <a class="btn btn-teal" style="left:616px;top:3654px;width:109px">PATIENT</a>
</section>

<!-- footer -->
<footer class="abs footer">
  <div class="logo" style="left:97px;top:62px">
    <span class="logo-dot" style="background:#fff;width:34px;height:34px"></span>
    <span class="logo-name" style="color:#fff;font-size:44px;letter-spacing:16px">QMT</span>
  </div>
  <div class="col">
    <a style="left:590px;top:49px">Home</a>
    <a style="left:590px;top:79px">Services</a>
    <a style="left:590px;top:109px">Articles</a>
  </div>
  <div class="log">
    <a style="left:777px;top:54px">Login &nbsp;As A Therapists</a>
    <a style="left:777px;top:84px">Login &nbsp;As A Patient</a>
  </div>
  <div class="abs" style="left:97px;top:171px;width:996px;height:1px;background:rgba(255,255,255,.6)"></div>
  <p class="abs" style="left:97px;top:191px;font-size:12.5px">©Copyright 2022. <u>QUIET MEADOW THERAPY</u> | All Rights Reserved</p>
</footer>
<span class="social" style="left:966px"></span>
<span class="social" style="left:1001px"></span>
<span class="social" style="left:1035px"></span>
<span class="social" style="left:1069px"></span>

</body>
</html>
```